Spaces That Serve - Invitation

Need a three fold, 8.5 X 11 invitation that will be direct mail for a seminar. We develop properties for churches in the United States. Final design should communicate a compelling reason for church leaders to attend the "Spaces That Serve" seminar. To be clear, the folded and complete invitation is 8.5" X 11" so there are a total of 6 panels measuring 8.5" X 11". Thanks and have fun.
Updates

Went on vacation/holiday

Target Market(s)

Young start up churches, highly energetic, not traditional at all.

Colors
0054AA
0677BA
7BADD7
CADEEF
E8F1F8
FFF300
FFF600
FEFA6F
FFFEC7
FFFEE8
FFC000
F8CF3A
FAE287
FDF2CF
FEFAEE
EB3D1F
EC4F4E
F09395
F8D3D4
FCEDEE

Requirements
Must have
• See the mock up brochure that I made up. It has all the info I need.
Nice to have
• Open space. Mock up is much too busy looking. Gives me a headache!
Should not have
• Nothing traditional church looking.

```html
<!DOCTYPE html>
<html lang="en">
<head>
<meta charset="utf-8">
<title>Spaces That Serve – Seminar Invitation</title>
<link href="https://fonts.googleapis.com/css2?family=Poppins:wght@400;500;600;700;800&display=swap" rel="stylesheet">
<style>
:root{
  --blue:#1b5fae;
  --blue-dark:#0054AA;
  --orange:#ec6a3c;
  --ink:#2b2b2b;
  --panel:#f2f2f3;
  --paper:#ffffff;
  --page:#ffffff;
}
*{box-sizing:border-box;margin:0;padding:0}
html,body{width:869px;height:1200px;overflow:hidden;background:var(--page)}
body{font-family:"Poppins",sans-serif;color:var(--ink);position:relative}
.spread{position:absolute;width:740px;height:572px;display:grid;grid-template-columns:repeat(3,1fr);background:var(--panel);box-shadow:0 14px 18px -10px rgba(0,0,0,.25)}
.spread--outer{left:18px;top:18px}
.spread--inner{left:111px;top:610px}
.panel{position:relative;padding:16px 16px 0;overflow:hidden}
.panel--cover{background:var(--paper);text-align:center;padding:14px 12px 0}
.photo{position:absolute}
h1.cover-title{font-weight:800;font-size:28px;color:var(--blue);letter-spacing:.5px;line-height:1.1}
.cover-sub{font-size:10px;margin-top:5px}
.cover-lead{font-weight:700;font-size:12.5px;color:var(--blue);line-height:1.25;margin-top:8px}
.cover-body{font-size:11px;line-height:1.25;margin-top:9px}
.cover-date{font-weight:700;font-size:8.5px;color:var(--blue);margin-top:8px}
.cities{display:flex;justify-content:space-between;border:1px solid var(--blue);margin:9px 4px 0;padding:3px 4px;font-size:7px;font-weight:600;color:var(--blue)}
h2{font-weight:700;color:var(--blue);line-height:1.2}
.h-sm{font-size:12px}
.h-md{font-size:13px}
.h-lg{font-size:21px;line-height:1.2}
.h-orange{color:var(--orange)}
.brand{font-weight:800;font-size:27px;color:var(--orange);line-height:1;margin-top:4px}
.brand-sub{font-weight:700;font-size:10.5px;color:var(--blue);border-bottom:1px solid var(--blue);display:inline-block}
.small-blue{font-size:8px;color:var(--blue);line-height:1.25}
.contact-head{font-weight:700;font-size:11px;color:var(--blue);margin-top:6px}
.contact-line{font-size:12px;color:var(--blue);line-height:1.15}
.contact-web{font-weight:700;font-size:12px;color:var(--orange)}
.phone{font-weight:800;font-size:22px;color:var(--orange);line-height:1.2}
.body{font-size:7px;line-height:1.7}
.body-blue{font-size:8.2px;line-height:1.35;color:var(--blue)}
.quote{font-size:6.5px;color:var(--orange);line-height:1.3;margin-top:3px}
.checklist{list-style:none;margin-top:8px}
.checklist li{position:relative;padding-left:13px;font-size:8.5px;color:var(--blue);line-height:1.2;margin-bottom:6px}
.checklist li::before{content:"";position:absolute;left:0;top:2px;width:6px;height:6px;background:var(--orange)}
.topics{display:grid;grid-template-columns:1fr 1fr;column-gap:12px;row-gap:6px;margin-top:9px}
.topics span{font-size:5.6px;color:var(--orange);line-height:1.25}
.mailing{font-weight:700;font-size:12px;color:var(--blue);margin-top:12px}
.rule{height:4px;width:146px;background:var(--blue-dark);margin:8px 0 14px}
.rule--orange{height:2px;background:var(--orange);width:180px;margin:7px 0 14px}
.speaker-title{font-weight:700;font-size:22px;line-height:1.15;color:var(--orange);letter-spacing:.5px}
.team{font-weight:700;font-size:12px;color:var(--orange);margin-top:8px}
.mt4{margin-top:4px}.mt8{margin-top:8px}.mt12{margin-top:12px}.mt16{margin-top:16px}
</style>
</head>
<body>

<!-- Outside of the invitation -->
<section class="spread spread--outer">
  <div class="panel panel--cover">
    <h1 class="cover-title">PASTOR! LEAD</h1>
    <p class="cover-sub">YOUR CHURCH WITH CONFIDENCE.</p>
    <p class="cover-lead">Attend the Spaces That Serve<br>Seminar Learn how to</p>
    <p class="cover-body">DESIGN, FINANCE and BUILD the most creative, functional and affordable church facilities in America!</p>
    <p class="cover-date">Coming to the Bay Area, March 4-7</p>
    <div class="cities"><span>Santa Rosa</span><span>Walnut Creek</span><span>San Jose</span><span>San Mateo</span></div>
    <div class="photo" role="img" aria-label="Church leaders seated at tables in a bright seminar room" style="left:0;right:0;bottom:0;height:225px;background:linear-gradient(180deg,#f4f8fb 0%,#b9d4e6 30%,#5f86a8 62%,#22344a 100%)"></div>
  </div>

  <div class="panel">
    <h2 class="h-sm">Seminar cost is just $29<br>and includes lunch!</h2>
    <div class="brand">MARLOW</div>
    <div class="brand-sub">Facility Solutions</div>
    <p class="small-blue mt4">Daniel R. Marlow America's<br>#1 Church Developer</p>
    <p class="contact-head">Contact Dan Marlow to register.</p>
    <p class="contact-line">Seating is limited</p>
    <p class="contact-web">danmarlow.com</p>
    <p class="contact-line">dan@danmarlow.com</p>
    <p class="phone">555-204-7718</p>
    <p class="body mt4">I remember sitting at my desk back in 2001, wondering what am I going to do? Wishing that there was someone I could call that had the knowledge and experience to guide me in the right direction. That is when a seminar invitation showed up on my desk and I soon met Dan Marlow.<br>Since then, The Grove Fellowship has gone through numerous building programs, grown to over 5,000 in attendance and grown into a thriving ministry with a high global impact.</p>
    <div class="photo" role="img" aria-label="Worship service in a large auditorium with purple stage lighting" style="left:0;right:0;bottom:0;height:208px;background:linear-gradient(180deg,#2a1d33 0%,#8a3f9e 35%,#5a2e62 60%,#2b1f1c 100%)"></div>
  </div>

  <div class="panel">
    <h2 class="h-sm">Here's the bad news:</h2>
    <p class="body mt4">The average tenure of a pastor after a significant building project is twenty-two months. Over half of the churches in the U.S. have a set of plans (stuck behind the pastor's door) that will never be built. To top it off, construction is the second most litigated industry in the U.S., behind medical. Some pastors will deal with these statistics by never building. Some will forge ahead alone and often become one of these statistics. The good news is that others will seek out those who have built to gain counsel and wisdom.</p>
    <p class="quote">"Plans fail for lack of counsel, but with many advisors they succeed" Proverbs 15:22</p>
    <h2 class="h-sm mt12">We help Pastors and church leaders to:</h2>
    <ul class="checklist">
      <li>Develop state of the art facilities that are functional &amp; affordable</li>
      <li>Reduce the stress and distractions of a building program</li>
      <li>Avoid the pitfalls of typical building projects</li>
      <li>Eliminate those unexpected surprises.</li>
      <li>Maximize Ministry Momentum by eliminating growth barriers.</li>
    </ul>
    <h2 class="h-sm">The seminar teaches a variety of topics including:</h2>
    <div class="topics">
      <span>10-Steps to Your<br>New Facility</span><span>Meet Your<br>Development Team</span>
      <span>Creative Land<br>Acquisition</span><span>Deal Free<br>Development</span>
      <span>Funding Your<br>Building Program</span><span>Understanding the<br>Permit Process</span>
      <span>What Type of Building<br>Right for You</span><span>Dealing with Nasty<br>Neighbors</span>
      <span>Creative Church<br>Designs</span><span>Developing a<br>Communication Plan</span>
      <span>Time and Talent<br>Surveys</span><span>Master Planning<br>Your Campus</span>
    </div>
    <p class="mailing">Mailing info goes here.</p>
  </div>
</section>

<!-- Inside of the invitation -->
<section class="spread spread--inner">
  <div class="panel">
    <h2 class="h-sm">Feeling a bit overwhelmed?</h2>
    <p class="body-blue mt4">We get it. God is growing your ministry, but your current facilities cannot sustain it.</p>
    <p class="body-blue mt12">Where do you start? Who do you call? What are you going to do?</p>
    <h2 class="h-sm h-orange mt8">ASKING GOD FOR GUIDANCE AND DIRECTION?</h2>
    <p class="body mt12">You need a Kingdom focused ally with over forty years experience developing hundreds of state-of-the-art, Christian church facilities all across America</p>
    <h2 class="h-lg mt16">That is where we come in!</h2>
    <p class="body-blue mt12" style="line-height:1.8">Discover the possibilities you may not even know exist and then seize your God-given potential!</p>
    <div class="photo" role="img" aria-label="Modern church building exterior with palm trees" style="left:0;width:150px;bottom:72px;height:134px;background:linear-gradient(160deg,#9fb9d2,#6d7c83 55%,#3d4a35)"></div>
    <div class="photo" role="img" aria-label="Church campus building" style="left:154px;right:0;bottom:142px;height:64px;background:linear-gradient(180deg,#cfd8de,#8b7a6e)"></div>
    <div class="photo" style="left:154px;right:0;bottom:72px;height:66px;background:#e88f6d" role="img" aria-label="Church facade with orange tint"></div>
    <div class="photo" role="img" aria-label="Construction site at sunset" style="left:0;right:0;bottom:0;height:68px;background:linear-gradient(180deg,#6b8ea8,#e6a64e 70%,#3a2a1a)"></div>
  </div>

  <div class="panel">
    <h2 class="speaker-title">ABOUT OUR<br>SPEAKER</h2>
    <div class="rule"></div>
    <p class="body">Dan Marlow, founder of Marlow Facility Solutions, is America's top developer of Christian church facilities. Beginning in 1980, Dan has used his wisdom and experience to help ministries like yours to overcome the challenges to their facility needs and growth barriers. Dan's unique understanding of ministry needs make him a trusted partner for churches that need functional and affordable facilities that are designed to grow with them.</p>
    <h2 class="h-sm mt16">Learn from the experience<br>of others!</h2>
    <div class="rule rule--orange"></div>
    <p class="body">If you are looking for expert guidance and direction in the design, finance and construction of your new, expanded or remodeled facilities, then this is your opportunity to lean from the nations leading expert on church design, finance and construction.</p>
    <div class="photo" role="img" aria-label="Church lobby interior with warm lighting" style="left:8px;width:164px;bottom:74px;height:108px;background:linear-gradient(170deg,#3a3024,#b68a3e 45%,#e7c27a 70%,#5a4328)"></div>
    <div class="photo" role="img" aria-label="Church building with blue tint" style="left:176px;right:0;bottom:74px;height:108px;background:#4a76b0"></div>
    <div class="photo" role="img" aria-label="Row of church buildings on a campus" style="left:8px;right:0;bottom:0;height:70px;background:linear-gradient(180deg,#a9bfd3,#5e6466 60%,#8d8a84)"></div>
  </div>

  <div class="panel">
    <h2 class="h-sm">Maximize your ministry potential for greater Kingdom impact!</h2>
    <p class="body-blue mt8">Cast a clear and compelling vision for the future and build a road map connecting our current reality to your future potential!</p>
    <h2 class="h-sm h-orange mt12" style="font-size:11px">WHO SHOULD ATTEND?</h2>
    <p class="body mt8">Whether you are looking to relocate, expand, remodel or build new, this seminar will equip you with the tools and confidence you need</p>
    <p class="small-blue mt4" style="font-size:6.5px;font-weight:500">Pastors, elders, church staff and volunteers are all invited!</p>
    <p class="team">BRING YOUR ENTIRE TEAM!</p>
    <div class="photo" role="img" aria-label="Church campus with playground and lawn" style="left:0;width:160px;bottom:116px;height:166px;background:linear-gradient(180deg,#7fa6cf,#b7b0a2 45%,#4f7a3a)"></div>
    <div class="photo" role="img" aria-label="Church entrance with orange tint" style="left:164px;right:0;bottom:116px;height:166px;background:#e48a63"></div>
    <div class="photo" role="img" aria-label="Church building under a blue sky" style="left:0;right:0;bottom:0;height:112px;background:linear-gradient(180deg,#2f6fb8,#a7c7e6 45%,#b49a7a 70%,#7a7a72)"></div>
  </div>
</section>

</body>
</html>
```